VaxLorn Customer Profile PDF Template

We want to develop a template that matches our branding theme for our product. The template will be a DPF template that is sent to dealers, distributors, and agents to complete when they sell our product. It will tel us about the buyer who purchased the equipment we sell. Template should include:
• Category boxes to check type of industry our equipment was sold to
1) Pharmaceutical/Nutraceutical
2) Food & Beverage
3) Chemical
4) Health & Beauty / Cosmetic
• A dedicated area to insert 3 to 4 pictures of product
• Form Info should also include
1)Company Name:
2)Website:
3)Location
4)Number of Locations
5)Number of Employees
6)Number of Products Made
7)VaxLorn Model
8)Serial Number
9)Date Ordered
10)Description of Use:
I have included our current form we hate, the current marketing ad we love, which communicated our theme perfectly,
Look and feel
Each slider illustrates characteristics of the customer's brand and the style your logo design should communicate.

```html
<!DOCTYPE html>
<html lang="en">
<head>
<meta charset="utf-8">
<title>VaxLorn Customer Profile</title>
<link href="https://fonts.googleapis.com/css2?family=Roboto+Condensed:ital,wght@1,400;1,700&family=Montserrat:wght@600&display=swap" rel="stylesheet">
<style>
  :root {
    --ink: #05080d;
    --navy: #0b2f52;
    --glow: #0f4f80;
    --red: #e30c1b;
    --blue: #1a72b8;
    --white: #ffffff;
    --field-border: #d2121f;
  }
  * { margin: 0; padding: 0; box-sizing: border-box; }
  html, body { width: 848px; height: 1200px; overflow: hidden; background: var(--ink); }
  .sheet {
    position: relative;
    width: 848px;
    height: 1200px;
    overflow: hidden;
    background:
      radial-gradient(ellipse 520px 420px at 50% 46%, var(--glow) 0%, var(--navy) 38%, #071524 70%, var(--ink) 100%);
    font-family: "Roboto Condensed", "Arial Narrow", sans-serif;
    color: var(--white);
  }
  .header-swoosh { position: absolute; left: 0; top: 0; width: 848px; height: 220px; }
  .brand {
    position: absolute;
    right: 42px;
    top: 38px;
    display: flex;
    align-items: center;
    gap: 12px;
    font-family: "Montserrat", sans-serif;
    font-weight: 600;
    font-size: 52px;
    color: var(--red);
    letter-spacing: 0.5px;
  }
  .brand-dot { width: 30px; height: 30px; border-radius: 50%; background: var(--blue); }
  .section-title {
    position: absolute;
    left: 0;
    width: 848px;
    text-align: center;
    font-style: italic;
    font-weight: 700;
    font-size: 30px;
    letter-spacing: 0.2px;
  }
  .section-title::after {
    content: "";
    position: absolute;
    left: 406px;
    bottom: -10px;
    width: 36px;
    height: 3px;
    background: var(--red);
  }
  .title-industry { top: 232px; }
  .title-products { top: 372px; }
  .title-information { top: 670px; }
  .industry-option { position: absolute; top: 304px; display: flex; gap: 12px; }
  .checkbox {
    width: 23px; height: 23px;
    background: var(--white);
    border: 2px solid var(--field-border);
    flex: none;
    margin-top: 2px;
  }
  .option-label { font-style: italic; font-size: 14px; line-height: 17px; text-transform: uppercase; }
  .photo-area { position: absolute; left: 40px; top: 430px; width: 768px; height: 230px; }
  .field-label {
    position: absolute;
    font-style: italic;
    font-size: 14px;
    text-transform: uppercase;
    letter-spacing: 0.1px;
  }
  .field {
    position: absolute;
    background: var(--white);
    border: 2px solid var(--field-border);
    height: 25px;
    width: 321px;
  }
  .col-left.field-label { left: 70px; }
  .col-left.field { left: 84px; }
  .col-right.field-label { left: 449px; }
  .col-right.field { left: 463px; }
  .field-tall { height: 92px; }
  .field-description { height: 207px; }
</style>
</head>
<body>
<main class="sheet">
  <svg class="header-swoosh" viewBox="0 0 848 220" aria-hidden="true">
    <path d="M0,0 H848 V176 C560,160 300,100 160,0 Z" fill="#ffffff"/>
    <path d="M0,0 H160 C300,100 560,160 848,176 C560,198 250,150 0,30 Z" fill="#000000"/>
    <path d="M0,0 H164 C304,102 562,162 846,177 C560,190 250,140 0,24 Z" fill="#e30c1b"/>
    <path d="M0,30 C250,150 560,198 848,176" fill="none" stroke="#1a72b8" stroke-width="7"/>
  </svg>

  <div class="brand"><span class="brand-dot"></span>VaxLorn</div>

  <h2 class="section-title title-industry">TYPE OF INDUSTRY</h2>

  <label class="industry-option" style="left:90px"><span class="checkbox"></span><span class="option-label">Pharmaceutical<br>/ Nutraceutical</span></label>
  <label class="industry-option" style="left:278px"><span class="checkbox"></span><span class="option-label">Food &amp; Beverage</span></label>
  <label class="industry-option" style="left:467px"><span class="checkbox"></span><span class="option-label">Chemical</span></label>
  <label class="industry-option" style="left:595px"><span class="checkbox"></span><span class="option-label">Health &amp; Beauty<br>/ Cosmetic</span></label>

  <h2 class="section-title title-products">PRODUCTS</h2>
  <div class="photo-area" role="img" aria-label="Space for three to four product photographs"></div>

  <h2 class="section-title title-information">INFORMATION</h2>

  <span class="field-label col-left" style="top:740px">Company Name</span>
  <span class="field col-left" style="top:762px"></span>
  <span class="field-label col-left" style="top:797px">Website</span>
  <span class="field col-left" style="top:821px"></span>
  <span class="field-label col-left" style="top:854px">Location</span>
  <span class="field col-left" style="top:877px"></span>
  <span class="field-label col-left" style="top:911px">Number of Locations</span>
  <span class="field col-left" style="top:935px"></span>
  <span class="field-label col-left" style="top:968px">Number of Employees</span>
  <span class="field col-left" style="top:992px"></span>
  <span class="field-label col-left" style="top:1025px">Number of Products Made</span>
  <span class="field field-tall col-left" style="top:1051px"></span>

  <span class="field-label col-right" style="top:740px">VaxLorn Model</span>
  <span class="field col-right" style="top:762px"></span>
  <span class="field-label col-right" style="top:797px">Serial Number</span>
  <span class="field col-right" style="top:821px"></span>
  <span class="field-label col-right" style="top:854px">Date Ordered</span>
  <span class="field col-right" style="top:877px"></span>
  <span class="field-label col-right" style="top:911px">Description of Use</span>
  <span class="field field-description col-right" style="top:936px"></span>
</main>
</body>
</html>
```